Lumora business card for a plastic surgeon

we need a business card for plastic surgeons that work on a clinic called LUMORA.
we want a clean design and the following informations: name of the doctor, doctor's registration number (called CRM), telephone, address, facebook, instagram.
Colors: white, blue tones, light brown/ coffee

facebook and instagram: lumoraesteticaclinica

Industry/Entity Type

Business

Contact Information for Business Card

clean design

Font styles to use
Serif
Sans Serif
Other font styles liked:
• helvetica light

Colors
cee9f5
85cae6
85abd2
3276b5
cfeae6
cedeed
eaf1f7

Requirements
Must have
• doctor's name
• identification number (called CRM)
• contact (phone, facebook, instagram, address)

```html
<!DOCTYPE html>
<html lang="en">
<head>
<meta charset="utf-8">
<title>Lumora business card</title>
<link rel="stylesheet" href="https://fonts.googleapis.com/css2?family=Cinzel:wght@400;600&family=Arimo:wght@400&display=swap">
<style>
  :root {
    --stage: #e9ecef;
    --coffee: #b09a86;
    --navy: #163a6b;
    --cyan: #2bbcdc;
    --white: #ffffff;
    --shadow: rgba(20, 30, 45, 0.18);
  }
  html, body {
    margin: 0;
    padding: 0;
    width: 1200px;
    height: 900px;
    overflow: hidden;
    background: var(--stage);
  }
  .canvas {
    position: relative;
    width: 1200px;
    height: 900px;
  }
  .card {
    position: absolute;
    width: 560px;
    height: 320px;
    border-radius: 22px;
    overflow: hidden;
    box-shadow: 0 12px 30px var(--shadow);
  }
  .card-back {
    left: 90px;
    top: 80px;
    background: var(--coffee);
  }
  .card-front {
    left: 550px;
    top: 490px;
    background: var(--white);
  }
  .back-name {
    position: absolute;
    left: 0;
    right: 0;
    top: 104px;
    text-align: center;
    font-family: "Cinzel", serif;
    font-weight: 400;
    font-size: 70px;
    letter-spacing: 4px;
    color: var(--white);
  }
  .socials {
    position: absolute;
    left: 34px;
    bottom: 30px;
    display: flex;
    align-items: center;
    gap: 12px;
  }
  .social-dot {
    width: 26px;
    height: 26px;
    border-radius: 50%;
    background: var(--white);
    opacity: 0.85;
  }
  .social-lines {
    font-family: "Arimo", sans-serif;
    font-size: 14px;
    line-height: 19px;
    color: var(--white);
  }
  .front-art {
    position: absolute;
    inset: 0;
  }
  .front-name {
    position: absolute;
    left: 34px;
    top: 34px;
    font-family: "Cinzel", serif;
    font-weight: 400;
    font-size: 52px;
    letter-spacing: 3px;
    color: var(--cyan);
  }
  .doctor {
    position: absolute;
    left: 34px;
    top: 126px;
    font-family: "Cinzel", serif;
    font-weight: 600;
    font-size: 23px;
    color: var(--navy);
    letter-spacing: 1px;
  }
  .doctor .title { color: var(--cyan); }
  .address {
    position: absolute;
    left: 34px;
    top: 168px;
    display: flex;
    align-items: center;
    gap: 12px;
    font-family: "Arimo", sans-serif;
    font-size: 14px;
    line-height: 18px;
    color: var(--navy);
  }
  .contacts {
    position: absolute;
    left: 34px;
    top: 250px;
    font-family: "Arimo", sans-serif;
    font-size: 14px;
    line-height: 19px;
    color: var(--white);
  }
  .contact-row {
    display: flex;
    align-items: center;
    gap: 9px;
  }
  .crm {
    position: absolute;
    right: 30px;
    top: 212px;
    font-family: "Cinzel", serif;
    font-size: 16px;
    color: var(--white);
  }
  .crm .label { color: var(--cyan); }
</style>
</head>
<body>
<main class="canvas">

  <section class="card card-back" aria-label="Card back">
    <div class="back-name">LUMORA</div>
    <div class="socials">
      <span class="social-dot"></span>
      <div class="social-lines">
        <div>facebook/lumoraesteticaclinica</div>
        <div>@lumoraesteticaclinica</div>
      </div>
    </div>
  </section>

  <section class="card card-front" aria-label="Card front">
    <svg class="front-art" width="560" height="320" viewBox="0 0 560 320" aria-hidden="true">
      <path d="M0 236 H190 L232 176 H560 V320 H0 Z" fill="var(--navy)"/>
      <line x1="232" y1="176" x2="560" y2="76" stroke="var(--cyan)" stroke-width="2"/>
      <circle cx="500" cy="150" r="62" fill="var(--cyan)"/>
    </svg>

    <div class="front-name">LUMORA</div>

    <div class="doctor"><span class="title">Dr.</span> Rafael Duarte</div>

    <div class="address">
      <svg width="24" height="22" viewBox="0 0 24 22" aria-hidden="true">
        <path d="M12 2 L22 11 H19 V20 H14 V14 H10 V20 H5 V11 H2 Z" fill="var(--cyan)"/>
      </svg>
      <div>
        <div>4715 Harbor Crest Way</div>
        <div>Coral Bay FL 33190</div>
      </div>
    </div>

    <div class="contacts">
      <div class="contact-row">
        <svg width="11" height="11" viewBox="0 0 12 12" aria-hidden="true"><path d="M2 1 L4.5 1 L5.5 3.5 L4 4.8 C4.8 6.5 5.7 7.4 7.2 8 L8.5 6.5 L11 7.5 V10 C6 11 1 6 2 1 Z" fill="var(--cyan)"/></svg>
        <span>+330 5518-2093</span>
      </div>
      <div class="contact-row">
        <svg width="11" height="11" viewBox="0 0 12 12" aria-hidden="true"><rect x="1" y="2.5" width="10" height="7" fill="none" stroke="var(--cyan)" stroke-width="1.3"/><path d="M1 2.5 L6 6.5 L11 2.5" fill="none" stroke="var(--cyan)" stroke-width="1.3"/></svg>
        <span>info@lumoraesteticaclinica.com</span>
      </div>
      <div class="contact-row">
        <svg width="11" height="11" viewBox="0 0 12 12" aria-hidden="true"><circle cx="6" cy="6" r="5" fill="none" stroke="var(--cyan)" stroke-width="1.3"/><path d="M1 6 H11 M6 1 C3.5 4 3.5 8 6 11 M6 1 C8.5 4 8.5 8 6 11" fill="none" stroke="var(--cyan)" stroke-width="1"/></svg>
        <span>www.lumoraesteticaclinica.com</span>
      </div>
    </div>

    <div class="crm"><span class="label">CRM</span>-48215</div>
  </section>

</main>
</body>
</html>
```